Sidewalk Sign For Laundry Service

I'd like to make a sign that offers *free* laundry service for the next customers that bring in their laundry. There needs to be some immediacy in the design. The idea is to put out this sign when we are idle in the laundry and want to use the time to attract new customers. So somehow we need to communicate that the offer is for right now and will likely be gone in an hour or two. Attached are photos of the sign holder in place to give a feel for the location and environment. Obviously I'm looking for a much better design that the one currently in use.

Requirements:
* 23.25" x 35.5" - the full width will be visible but the top and bottom 0.5" will be hidden by the sign holder. It will be printed on coroplast.
* Must include a large arrow to show where the service is offered. We're off the main street so the arrow helps a lot. See the attached pictures of the sign being replaced.
* Needs to be visible to cars as they drive by.
* For the final product I'll need three versions. One with an arrow pointing to the right, one with an arrow pointing to the left, and one to go in the store window with no arrow.

Background on the service: We sort, wash, dry, and fold the laundry for customers and then neatly put it in a nice laundry bag that makes returning very convenient. Their laundry comes out fresh, clean, smelling great, and without the hassle of doing it themselves. We have a great return rate. Most customers that try out the service become long term customers.

Attached are two pictures of the sign holder with our current "Laundry Wash & Fold" sign. Also, our logo which would be nice to include to help with branding.

```html
<!DOCTYPE html>
<html lang="en">
<head>
<meta charset="utf-8">
<title>Free Laundry Service – Sidewalk Sign</title>
<link rel="stylesheet" href="https://fonts.googleapis.com/css2?family=Archivo:wdth,wght@125,900&display=swap">
<style>
  :root {
    --navy: #2a3878;
    --navy-deep: #253270;
    --cyan-glow: #17a9d9;
    --mid-blue: #1f6fae;
    --orange: #ec6a2c;
    --orange-light: #f27e33;
    --shadow: #0d0d0d;
    --curl: #3a1812;
    --pole-light: #d9d9db;
    --pole-dark: #8d8d90;
    --white: #ffffff;
    --ink: #111111;
    --logo-square: #8cbde6;
  }
  html, body {
    margin: 0;
    padding: 0;
    overflow: hidden;
    background: var(--navy);
  }
  .sign {
    display: block;
    width: 776px;
    height: 1200px;
  }
  .headline {
    font-family: "Archivo", "Arial Black", sans-serif;
    font-weight: 900;
    font-stretch: 125%;
    fill: var(--white);
    stroke: var(--ink);
    stroke-width: 5;
    stroke-linejoin: round;
    paint-order: stroke fill;
  }
  .brand-name {
    font-family: "Archivo", "Arial Black", sans-serif;
    font-weight: 900;
    font-stretch: 125%;
    fill: var(--white);
  }
  .sparkle { fill: var(--white); }
</style>
</head>
<body>
<svg class="sign" viewBox="0 0 776 1200" xmlns="http://www.w3.org/2000/svg" role="img" aria-label="Free laundry service for the next 3 customers, arrow pointing right to Rinse on Maple">
  <defs>
    <radialGradient id="bgGlow" cx="430" cy="640" r="560" gradientUnits="userSpaceOnUse">
      <stop offset="0" stop-color="var(--cyan-glow)"/>
      <stop offset="0.45" stop-color="var(--mid-blue)"/>
      <stop offset="1" stop-color="var(--navy-deep)"/>
    </radialGradient>
    <linearGradient id="poleShade" x1="0" x2="1">
      <stop offset="0" stop-color="var(--pole-dark)"/>
      <stop offset="0.45" stop-color="var(--pole-light)"/>
      <stop offset="1" stop-color="var(--pole-dark)"/>
    </linearGradient>
    <linearGradient id="arrowShade" x1="0" x2="1">
      <stop offset="0" stop-color="var(--orange-light)"/>
      <stop offset="1" stop-color="var(--orange)"/>
    </linearGradient>
  </defs>

  <!-- background panel -->
  <rect class="backdrop" width="776" height="1200" fill="url(#bgGlow)"/>
  <rect class="pole" x="0" y="0" width="56" height="1200" fill="url(#poleShade)"/>

  <!-- ribbon arrow -->
  <g class="ribbon-arrow">
    <path class="ribbon-curl" d="M38 420 C10 430 8 520 30 545 C42 556 56 552 56 552 L56 440 Z" fill="var(--curl)"/>
    <path class="arrow-shadow" d="M22 148 L652 148 L652 80 L776 280 L652 522 L652 455 L56 455 L56 430 Q30 430 22 448 Z" fill="var(--shadow)"/>
    <path class="arrow-body" d="M14 138 L645 138 L645 72 L768 270 L645 512 L645 445 L50 445 Q20 445 14 470 Z" fill="url(#arrowShade)" stroke="var(--white)" stroke-width="3" stroke-linejoin="round"/>
  </g>

  <!-- brand -->
  <g class="brand">
    <rect class="brand-mark" x="84" y="182" width="158" height="158" rx="6" fill="var(--logo-square)"/>
    <text class="brand-name" x="262" y="285" font-size="50" textLength="380" lengthAdjust="spacingAndGlyphs">Rinse on Maple</text>
  </g>

  <!-- offer -->
  <g class="offer">
    <text class="headline offer-free" x="140" y="675" font-size="196" textLength="593" lengthAdjust="spacingAndGlyphs">FREE</text>
    <text class="headline offer-line" x="130" y="799" font-size="104" textLength="550" lengthAdjust="spacingAndGlyphs">LAUNDRY</text>
    <text class="headline offer-line" x="164" y="888" font-size="104" textLength="502" lengthAdjust="spacingAndGlyphs">SERVICE</text>
    <text class="headline offer-count" x="159" y="1052" font-size="118" textLength="497" lengthAdjust="spacingAndGlyphs">NEXT 3</text>
    <text class="headline offer-who" x="159" y="1117" font-size="70" textLength="521" lengthAdjust="spacingAndGlyphs">CUSTOMERS</text>
  </g>

  <!-- sparkles -->
  <g class="sparkles">
    <path class="sparkle" d="M280 552 L205 502 L285 545 L310 475 L290 555 L355 600 L282 562 L250 610 Z"/>
    <path class="sparkle" d="M676 716 L615 690 L680 708 L722 676 L686 718 L760 752 L678 726 L652 770 Z"/>
    <path class="sparkle" d="M160 976 L88 942 L163 968 L198 910 L168 980 L226 1010 L160 986 L125 1040 Z"/>
  </g>
</svg>
</body>
</html>
```